Membership card Design

Hi I need a new membership card design for a social University club located in New Zealand. Our club name is called Maple Lantern Circle (MLCIR) and we provide a social hub for international students from Asia to meet local students. We are a non-profit organization that organizes activities such as paintball, ski trips, parties and day trips for our members. We need designs that look more like a membership card than a name card because we will be giving them to our members as a proof of membership. We would prefer a design that is simple in the front and with our club details, contacts and a place to write down a membership number on the back. We would like our card to have designs using the colours red, black, grey and orange. The design must incoporate the logo attached in this project. If possible, we would like the flower in the Hong Kong Flag to be incoporated in the design. The final design must look more like a membership card than a name card and communicate professionalism and high quality.
Updates

Target Market(s)

University Students

Industry/Entity Type

Non-Profit

Requirements
Must have
• The design must include:

The logo of our club
Our facebook page details: www.friendspage.example/maplelantern.cir
Our email: maplelanterncir@mailbox.example
A place behind the card to print membership numbers.

```html
<!DOCTYPE html>
<html lang="en">
<head>
<meta charset="utf-8">
<title>Maple Lantern Circle – Membership Card</title>
<link rel="stylesheet" href="https://fonts.googleapis.com/css2?family=Fondamento&family=Alegreya:ital,wght@0,400;0,700;1,400;1,700&family=Open+Sans&display=swap">
<style>
  :root {
    --red: #ff0000;
    --red-pale: #f9b3b3;
    --grey-dark: #444444;
    --grey-mid: #bdbdbd;
    --ink: #111111;
    --white: #ffffff;
    --stage-top: #e6e6e6;
    --stage-mid: #ffffff;
  }
  * { box-sizing: border-box; margin: 0; padding: 0; }
  html, body { width: 846px; height: 1200px; overflow: hidden; }
  body {
    position: relative;
    background: radial-gradient(ellipse at 50% 50%, var(--stage-mid) 0%, var(--stage-top) 100%);
    font-family: "Alegreya", serif;
    color: var(--ink);
  }
  .card {
    position: absolute;
    left: 14px;
    width: 810px;
    height: 540px;
    background: var(--white);
    box-shadow: 8px 9px 5px rgba(0,0,0,0.55);
    overflow: hidden;
  }
  .card--front { top: 13px; }
  .card--back { top: 627px; }

  /* front */
  .crest-backdrop {
    position: absolute; left: 0; top: 60px; width: 400px; height: 480px;
    background: radial-gradient(ellipse at 30% 30%, var(--red-pale) 0%, rgba(249,179,179,0.35) 45%, transparent 70%),
                radial-gradient(ellipse at 25% 85%, rgba(189,189,189,0.8) 0%, transparent 60%);
  }
  .club-title {
    position: absolute; left: 4px; top: 2px;
    font-family: "Fondamento", serif; font-size: 38px; line-height: 1;
    color: var(--grey-dark); letter-spacing: 0.5px; text-transform: uppercase;
  }
  .university-band {
    position: absolute; left: 0; top: 50px; width: 100%; height: 25px;
    background: var(--red); color: var(--white);
    font-family: "Open Sans", sans-serif; font-size: 22px; line-height: 25px; padding-left: 6px;
  }
  .photo-slot {
    position: absolute; left: 30px; top: 110px; width: 231px; height: 239px;
    background: var(--white); border: 2px solid var(--red); border-radius: 2px;
    box-shadow: 2px 2px 4px rgba(0,0,0,0.35);
    display: flex; align-items: center; justify-content: center;
    font-family: "Alegreya", serif; font-size: 20px;
  }
  .member-details {
    position: absolute; left: 297px; top: 186px;
    font-family: "Fondamento", serif; font-size: 38px; line-height: 40px;
  }
  .tagline {
    position: absolute; left: 10px; top: 485px;
    font-family: "Alegreya", serif; font-style: italic; font-weight: 700; font-size: 31px;
    transform: rotate(-10deg); transform-origin: left bottom; white-space: nowrap;
  }
  .club-mark {
    position: absolute; right: 8px; top: 470px;
    display: flex; align-items: center; gap: 10px;
    font-family: "Fondamento", serif; font-size: 34px; color: var(--red); white-space: nowrap;
  }
  .club-mark__dot { width: 34px; height: 34px; border-radius: 50%; background: var(--red); }

  /* back */
  .certification {
    position: absolute; left: 0; top: 68px; width: 100%;
    text-align: center; font-style: italic; font-size: 27px; line-height: 24px;
  }
  .signatory {
    position: absolute; top: 250px; width: 260px; text-align: center;
  }
  .signatory--president { left: 49px; }
  .signatory--vice { left: 492px; }
  .signatory__sign {
    display: inline-block; font-style: italic; font-weight: 700; font-size: 20px;
    transform: rotate(-12deg); margin-bottom: 32px;
  }
  .signatory__name { font-style: italic; font-weight: 700; font-size: 22px; line-height: 24px; }
  .signatory__role { font-style: italic; font-size: 17px; line-height: 18px; }
  .details-band {
    position: absolute; left: 0; top: 403px; width: 100%; height: 111px;
    background: var(--red); color: var(--white);
  }
  .details-band__code {
    position: absolute; left: 12px; top: 10px; font-size: 54px; line-height: 54px;
  }
  .details-band__number {
    position: absolute; left: 14px; top: 74px;
    font-style: italic; font-weight: 700; font-size: 21px;
  }
  .details-band__line {
    display: inline-block; width: 142px; border-bottom: 2px solid var(--white); margin-left: 6px;
  }
  .details-band__contacts {
    position: absolute; right: 10px; top: 30px; text-align: left;
    font-style: italic; font-size: 25px; line-height: 30px;
  }
</style>
</head>
<body>
  <section class="card card--front">
    <div class="crest-backdrop" role="img" aria-label="Faint red and grey club crest decoration"></div>
    <h1 class="club-title">Maple Lantern Circle</h1>
    <div class="university-band">Name of university here</div>
    <div class="photo-slot">picture of member</div>
    <div class="member-details">
      <p>Name of member</p>
      <p>Year joined</p>
    </div>
    <p class="tagline">Tagline, if you have any.</p>
    <div class="club-mark"><span class="club-mark__dot"></span>Maple Lantern Circle</div>
  </section>

  <section class="card card--back">
    <p class="certification">This certifies that the owner of this card is a bonafide<br>member of the Maple Lantern Circle.</p>
    <div class="signatory signatory--president">
      <span class="signatory__sign">signature</span>
      <p class="signatory__name">Name of President</p>
      <p class="signatory__role">President</p>
    </div>
    <div class="signatory signatory--vice">
      <span class="signatory__sign">signature</span>
      <p class="signatory__name">Name of Vice President</p>
      <p class="signatory__role">Vice President</p>
    </div>
    <div class="details-band">
      <p class="details-band__code">MLCIR</p>
      <p class="details-band__number">Membership #<span class="details-band__line"></span></p>
      <div class="details-band__contacts">
        <p>www.friendspage.example/maplelantern.cir</p>
        <p>maplelanterncir@mailbox.example</p>
      </div>
    </div>
  </section>
</body>
</html>
```